Concepts needed for Brochure design

Hi,

Looking for professional brochure design concepts to present our company's Training & Business Consultancy abilities as detailed and included in the 12 slide PowerPoint presentation.
Need to include all the information in the presentation, so looking at creative concept options to present this in a professional 4 page brochure with related images and color palette that matches our website www.ruvko.com.
Thanks,
Brent.

```html
<!DOCTYPE html>
<html lang="en">
<head>
<meta charset="utf-8">
<title>Lean Six Sigma Training &amp; Business Consultancy</title>
<link rel="stylesheet" href="https://fonts.googleapis.com/css2?family=PT+Sans:ital,wght@0,400;0,700;1,400;1,700&display=swap">
<style>
:root{
  --navy:#16506a;
  --sea:#2a7f9c;
  --sea-light:#3b93ad;
  --cell:#1f6f8b;
  --orange:#f7941d;
  --label:#1c5670;
  --white:#ffffff;
  --paper:#ffffff;
}
*{margin:0;padding:0;box-sizing:border-box}
html,body{width:848px;height:1200px;overflow:hidden;background:var(--paper)}
body{font-family:"PT Sans",Arial,sans-serif;color:var(--white);position:relative}
.backdrop{position:absolute;left:0;top:0;width:848px;height:545px}
.headline{position:absolute;left:34px;top:14px;font-size:40px;line-height:42px;font-weight:700;letter-spacing:-.2px}
.why{position:absolute;left:36px;top:136px;font-size:22px;font-weight:700}
.benefits{position:absolute;top:172px;font-size:12.2px;line-height:17px}
.benefits h3{font-style:italic;font-weight:400;font-size:15px;margin:0 0 14px 10px}
.benefits ul{list-style:none}
.benefits li{padding-left:10px;position:relative}
.benefits li::before{content:"•";position:absolute;left:0}
.benefits.individuals{left:16px;width:400px}
.benefits.business{left:426px;width:410px}
.model-title{position:absolute;left:26px;top:487px;font-size:38px;font-weight:700;white-space:nowrap}
.model-title em{font-weight:400;font-size:36px}
.row-label{position:absolute;left:36px;color:var(--label);font-style:italic;font-weight:700;font-size:12.5px}
.stage{position:absolute;top:551px;width:135px}
.stage-head{height:39px;background:var(--orange);text-align:center;font-size:18px;line-height:39px;font-weight:400;letter-spacing:.3px}
.stage-body{margin-top:10px;height:584px;background:var(--cell);padding:6px 6px 0 10px;font-size:12px;line-height:17px;display:grid;grid-template-rows:68px 239px 69px 80px 1fr}
.stage-body ul{list-style:none}
.stage-body li{padding-left:10px;position:relative}
.stage-body li::before{content:"•";position:absolute;left:0}
</style>
</head>
<body>
<svg class="backdrop" viewBox="0 0 848 545" aria-hidden="true">
  <rect width="848" height="545" fill="var(--navy)"/>
  <path d="M0 112 C180 78 420 150 620 108 C720 88 800 92 848 98 L848 455 C640 485 360 425 0 462 Z" fill="var(--sea)"/>
  <path d="M0 112 C180 78 420 150 620 108 C720 88 800 92 848 98 L848 122 C760 114 680 118 600 134 C420 168 200 104 0 140 Z" fill="var(--sea-light)" opacity=".55"/>
  <path d="M0 462 C360 425 640 485 848 455 L848 470 C640 500 360 440 0 478 Z" fill="var(--sea-light)" opacity=".35"/>
</svg>

<h1 class="headline">Globally Accredited Lean Six Sigma<br>Training &amp; Certification</h1>
<h2 class="why">Why Lean Six Sigma?</h2>

<section class="benefits individuals">
  <h3>Benefits for individuals</h3>
  <ul>
    <li>Decrease Operating costs while increasing quality &amp; output.</li>
    <li>Increase customer Loyalty and shareholder value.</li>
    <li>Improve skill retention.</li>
    <li>Streamline processes and Reduce ‘Waste’ &amp; ‘Variation’.</li>
    <li>Increase Customer satisfaction scores.</li>
    <li>Create a more sustainable business.</li>
    <li>Create an environment and cultire of change &amp; innovation in the organisation.</li>
    <li>Improve your employee engagement percentage.</li>
    <li>Be recognised as an ‘best-in-class’ organisation with sound values and a sustainable value chain delivery model.</li>
    <li>Continuously improve products, services and exceed customer expectations to become a market leader.</li>
  </ul>
</section>

<section class="benefits business">
  <h3>Benefits for Business</h3>
  <ul>
    <li>Gain Knowledge on advanced Business &amp; Process Improvement methodologies.</li>
    <li>Career Progression</li>
    <li>Ability to start thinking Strategically.</li>
    <li>Enable tactical improvements within your division / department / team.</li>
    <li>Lead Process Improvement initiatives.</li>
    <li>Improve your project management skills</li>
    <li>Master Stakeholder managemnet &amp; Change Management skills</li>
    <li>Use data to drive improvements withing your domains</li>
    <li>Assist Executive level Management to make informed decisions through use of statistical &amp; logical analysis.</li>
    <li>Improve your leadership skills and Team management abilities.</li>
  </ul>
</section>

<h2 class="model-title">Business Consultancy <em>– RUVKO Delivery Model</em></h2>

<div class="row-label" style="top:620px">Pre-requisite</div>
<div class="row-label" style="top:704px">Activities</div>
<div class="row-label" style="top:928px">Output</div>
<div class="row-label" style="top:996px">Control</div>
<div class="row-label" style="top:1081px">Tools</div>

<section class="stage" style="left:112px">
  <div class="stage-head">PLAN</div>
  <div class="stage-body">
    <ul><li>Formal intent to engage</li><li>Gather VOC</li></ul>
    <ul><li>Understand objective</li><li>Finalize process scope</li><li>Finalize scope of Data Collection</li><li>Estimate &amp; plan</li><li>Obtain Stakeholders’ buy-in</li><li>Define Governance structure</li></ul>
    <ul><li>Plan (Effort, Resource &amp; Schedule)</li><li>Guidelines</li></ul>
    <ul><li>Review of Scope &amp; plan with stakeholders</li></ul>
    <ul><li>Project charter</li><li>BPM Project handbook</li><li>Process scope capture template</li><li>Estimation template</li></ul>
  </div>
</section>

<section class="stage" style="left:255px">
  <div class="stage-head">INTROSPECT</div>
  <div class="stage-body">
    <ul><li>Signed-off Plan</li><li>Access to existing documentation</li></ul>
    <ul><li>Conduct workshops to understand Business process</li><li>Capture business &amp; operation processes (Level 1 to Level 5)</li><li>Capture issues, pain points , Suggestions, control points &amp; handoffs</li><li>Maturity Model Study</li><li>Cost Benefit Analysis</li></ul>
    <ul><li>Business Process Maps</li></ul>
    <ul><li>Validation of Business Process Map with Process SMEs</li></ul>
    <ul><li>Process capture template</li><li>Modeling standards</li><li>Review checklist</li></ul>
  </div>
</section>

<section class="stage" style="left:398px">
  <div class="stage-head">MOBILISE</div>
  <div class="stage-body">
    <ul><li>Validated Business process maps</li></ul>
    <ul><li>Capture attributes like volume, processing time ,Time &amp; Motion, No. of resources, TAT , exception and its type, training content etc</li><li>Conduct in depth process analysis and data analysis inclusive of hypothesis testing.</li><li>Cost Benefit Analysis</li></ul>
    <ul><li>Business Process updated with collection of data</li></ul>
    <ul><li>Validation of Data with Business</li></ul>
    <ul><li>Data collection template</li><li>Data attribute dictionary.</li><li>Statlyze</li></ul>
  </div>
</section>

<section class="stage" style="left:542px">
  <div class="stage-head">TEST</div>
  <div class="stage-body">
    <ul><li>Business Process Maps</li><li>Data Collected</li></ul>
    <ul><li>Subjective analysis and quantitative analysis</li><li>Identification of critical paths of the process</li><li>Identify risk inducing activities.</li><li>Develop ‘What-If’ scenarios.</li><li>Pilot / UAT/BVT</li><li>Cost Benefit Analysis</li></ul>
    <ul><li>Analysis Report</li></ul>
    <ul><li>Validation of analysis with Process owners</li></ul>
    <ul><li>Analysis capture template</li><li>Cost benefit analysis template</li></ul>
  </div>
</section>

<section class="stage" style="left:686px">
  <div class="stage-head">COMMISSION</div>
  <div class="stage-body">
    <ul><li>Validated Business Process Maps</li><li>Analysis Report</li></ul>
    <ul><li>Recommendations for automation, off shoring , process optimization , harmonization, standardization etc</li><li>Maturity Model study</li><li>Cost Benefit Analysis.</li><li>Control measures</li><li>Build Target operating Model</li></ul>
    <ul><li>To-Be process map</li><li>Recommendation &amp; Implementation plan</li></ul>
    <ul><li>Validation of recommendation</li><li>Report &amp; Implementation plan</li></ul>
    <ul><li>Recommendation report templates</li></ul>
  </div>
</section>
</body>
</html>
```